We Buy Houses Website

Looking for a highly motivated and skillfull designer to design and code me a "we Buy Houses" type website. I have a potential logo, but if you think you can make a BETTER one, please do try and incorporate it in your template. I am looking for creativity, professionalism, simple yet elegant. I will need a simple form on the front of the template along with pictures I provide you of recent houses I have bought. Look at these sites for examples of the layout of the website:

http://www.brickvalehomes.example/
http://www.petrafixeshouses.example/
http://www.quickpropertyexitnow.example/

If you make me a design that blows me away, and you are dependable, you will become part of my team and in charge of the web aspect which will include designing, updating, any and all graphics and logo work, SEO, coding. If you have skills in all of these areas please make me a design and lets do business!! The name of the website will be "Lurt Takes Homes" at LurtTakesHomes.example

I have uploaded some pictures of houses that we have done, please feel free to incorporate this into the banner or the design, etc. I want them to know we buy houses in ANY condition, as is, cash, can close immediately so they can get on with their life. We have many options to help them find a solution to whatever problem they have. We are in the business of helping people.

Target Market(s)

People looking to sell their houses
people facing foreclosure, bankruptcy, death in the family, divorce, anyone that we can help
people with ugly houses that need a lot of repair

Industry/Entity Type

Business

Font styles to use
Serif
Sans Serif

Colors

Designer to choose colors to be used in the design.

Requirements
Must have
• must have a simple form on the front of the page, preferrably near the banner, with the few required fields to help someone get started putting in their interest to sell their house, view the 2 websites i put as examples to see what kind of fields it should have.

My phone number (555) 482-1937 along with a Lurt Takes Homes logo, clean simple and elegant and professional. I want a nice color scheme that is not white but professional and has a wow factor.

```html
<!DOCTYPE html>
<html lang="en">
<head>
<meta charset="utf-8">
<title>Lurt Takes Homes</title>
<link href="https://fonts.googleapis.com/css2?family=Source+Sans+3:wght@300;400;600;700&display=swap" rel="stylesheet">
<style>
:root{
  --red:#e8302f;
  --red-dark:#c42423;
  --slate:#3f4e5a;
  --slate-deep:#2f3b45;
  --footer:#4a5a66;
  --ink:#3b3b3b;
  --muted:#6a6a6a;
  --white:#ffffff;
  --line:#d9d9d9;
}
*{box-sizing:border-box;margin:0;padding:0}
html,body{width:1200px;height:3340px;overflow:hidden}
body{position:relative;font-family:"Source Sans 3",sans-serif;color:var(--ink);background:var(--white)}
.abs{position:absolute}

/* header */
.site-header{position:absolute;left:0;top:0;width:1200px;height:120px;background:var(--white);border-top:6px solid var(--red)}
.brand{position:absolute;left:160px;top:28px;display:flex;align-items:center;gap:12px}
.brand-square{width:28px;height:28px;background:var(--red)}
.brand-name{font-size:26px;font-weight:700;color:var(--slate);letter-spacing:.2px}
.phone-box{position:absolute;left:478px;top:3px;width:36px;height:40px;background:var(--red);display:flex;align-items:center;justify-content:center}
.phone-number{position:absolute;left:520px;top:14px;font-size:17px;color:var(--muted)}
.social{position:absolute;left:660px;top:14px;display:flex;gap:13px}
.social span{display:block;width:22px;height:22px;border-radius:50%;background:#8a8f94}
.btn-sign{position:absolute;left:868px;top:10px;width:78px;height:28px;background:var(--red);color:var(--white);font-size:15px;display:flex;align-items:center;justify-content:center}
.btn-login{position:absolute;left:960px;top:10px;width:77px;height:28px;background:#e6e6e6;border:1px solid #bdbdbd;color:#333;font-size:15px;display:flex;align-items:center;justify-content:center}
.main-nav{position:absolute;top:72px;left:0;font-size:15px;color:var(--muted)}
.main-nav a{position:absolute;white-space:nowrap;color:inherit;text-decoration:none}
.main-nav a.active{color:var(--red)}

/* hero */
.hero{position:absolute;left:0;top:120px;width:1200px;height:655px;background:linear-gradient(180deg,#505d68 0%,#3e4a55 55%,#46525d 100%)}
.hero-title{position:absolute;left:160px;top:72px;font-size:64px;color:var(--white);font-weight:300;white-space:nowrap;line-height:1}
.hero-title b{font-weight:700}
.hero-lead{position:absolute;left:162px;top:150px;width:900px;font-size:20px;line-height:28px;color:#eef0f2}
.btn-ghost{position:absolute;border:2px solid var(--white);color:var(--white);font-size:19px;display:flex;align-items:center;justify-content:center}
.form-title{position:absolute;left:0;width:1200px;top:358px;text-align:center;font-size:38px;font-weight:700;color:var(--white);letter-spacing:.5px}
.form-rule{position:absolute;left:0;top:425px;width:1200px;height:1px;background:rgba(255,255,255,.35)}
.field{position:absolute;height:36px;background:var(--white);border:1px solid #cfcfcf;font-size:15px;color:#9a9a9a;padding:9px 8px}
.btn-submit{position:absolute;left:930px;top:547px;width:107px;height:36px;background:var(--red);color:var(--white);font-size:18px;font-weight:700;display:flex;align-items:center;justify-content:center;border:1px solid var(--red-dark)}

/* process */
.process{position:absolute;left:0;top:775px;width:1200px;height:489px;background:var(--white)}
.step-label{position:absolute;font-size:21px;font-weight:600;color:var(--slate);white-space:nowrap}
.step-label.red{color:var(--red);text-align:center;line-height:24px}
.step-circle{position:absolute;width:126px;height:126px;border-radius:50%;display:flex;align-items:center;justify-content:center}
.step-circle.slate{background:var(--slate)}
.step-circle.red{background:var(--red)}

/* we buy */
.we-buy{position:absolute;left:0;top:1264px;width:1200px;height:557px;background:linear-gradient(180deg,#e04a47 0%,#d83a38 60%,#d34644 100%)}
.section-title{position:absolute;font-size:34px;font-weight:700;color:var(--white);white-space:nowrap}
.we-buy-sub{position:absolute;right:163px;top:196px;font-size:31px;color:var(--white);white-space:nowrap}
.we-buy-text{position:absolute;right:163px;top:252px;width:520px;text-align:right;font-size:20px;line-height:26px;color:#fbe9e9}

/* features */
.features{position:absolute;left:0;top:1821px;width:1200px;height:605px;background:var(--white)}
.features h2{position:absolute;left:160px;top:130px;font-size:31px;font-weight:400;color:var(--ink)}
.features-lead{position:absolute;left:160px;top:186px;width:510px;font-size:19px;line-height:27px;color:var(--muted)}
.bullet-list{position:absolute;left:160px;top:290px;list-style:none}
.bullet-list li{position:relative;padding-left:28px;font-size:19px;color:var(--muted);height:38.5px}
.bullet-list li::before{content:"";position:absolute;left:2px;top:8px;width:12px;height:12px;border-radius:50%;background:var(--slate)}
.features-mark{position:absolute;left:640px;top:110px;width:470px;height:380px}

/* clients */
.clients{position:absolute;left:0;top:2426px;width:1200px;height:557px;background:linear-gradient(180deg,#1f262d 0%,#2a3139 50%,#222930 100%)}
.quote-mark{position:absolute;font-size:110px;line-height:1;color:#d8dadc;font-weight:300}
.clients-text{position:absolute;left:240px;top:218px;width:720px;text-align:center;font-size:20px;line-height:27px;color:#e9ebed}
.client-avatar{position:absolute;left:543px;top:343px;width:116px;height:116px;border-radius:50%;border:4px solid var(--white);background:linear-gradient(160deg,#d8dde2,#9aa6b0)}
.client-name{position:absolute;left:0;width:1200px;top:474px;text-align:center;font-size:19px;color:#e9ebed}

/* footer */
.site-footer{position:absolute;left:0;top:2983px;width:1200px;height:357px;background:var(--footer)}
.footer-skyline{position:absolute;left:0;top:222px;width:1200px;height:135px;background:linear-gradient(180deg,rgba(97,112,124,0) 0%,#5d6d79 40%,#647481 100%)}
.footer-head{position:absolute;top:60px;font-size:25px;font-weight:600;color:var(--white)}
.footer-rule{position:absolute;left:0;top:96px;width:1200px;height:1px;background:rgba(255,255,255,.25)}
.footer-about{position:absolute;left:162px;top:110px;width:230px;font-size:13px;line-height:16px;color:#e3e7ea}
.footer-nav{position:absolute;left:565px;top:110px;list-style:none;font-size:14px;line-height:23px;color:#e3e7ea}
.footer-social{position:absolute;left:888px;top:112px;display:flex;gap:8px}
.footer-social span{display:block;width:20px;height:20px;border-radius:50%;background:var(--white)}
.footer-brand{position:absolute;left:888px;top:152px;display:flex;align-items:center;gap:7px}
.footer-brand i{display:block;width:14px;height:14px;background:var(--white)}
.footer-brand span{font-size:14px;font-weight:700;color:var(--white)}
.footer-copy{position:absolute;left:888px;top:186px;font-size:12px;line-height:16px;color:#e3e7ea}
</style>
</head>
<body>

<header class="site-header">
  <div class="brand"><span class="brand-square"></span><span class="brand-name">Lurt Takes Homes</span></div>
  <div class="phone-box">
    <svg width="20" height="20" viewBox="0 0 24 24"><path d="M6.6 10.8a15 15 0 0 0 6.6 6.6l2.2-2.2a1 1 0 0 1 1-.25 11.4 11.4 0 0 0 3.6.57 1 1 0 0 1 1 1V20a1 1 0 0 1-1 1A17 17 0 0 1 3 4a1 1 0 0 1 1-1h3.5a1 1 0 0 1 1 1c0 1.25.2 2.45.57 3.57a1 1 0 0 1-.25 1z" fill="#fff"/></svg>
  </div>
  <div class="phone-number">(555) 482-1937</div>
  <div class="social" aria-label="Social links"><span></span><span></span><span></span><span></span><span></span></div>
  <div class="btn-sign">Sign Up</div>
  <div class="btn-login">Log in</div>
  <nav class="main-nav">
    <a class="active" style="left:476px">Home</a>
    <a style="left:545px">Sell My House</a>
    <a style="left:668px">Recent Projects</a>
    <a style="left:801px">How it Works</a>
    <a style="left:915px">About</a>
    <a style="left:986px">Contact</a>
  </nav>
</header>

<section class="hero" role="img" aria-label="Photo of a bright house interior with kitchen, dimmed under a slate overlay">
  <h1 class="hero-title">Welcome to <b>LURT TAKES HOMES</b></h1>
  <p class="hero-lead">This is Photoshop's version &nbsp;of Lorem Ipsum. Proin gravida nibh vel velit auctor alique Aenean sollicitudi orem quis bibendum auctor, nisi elit</p>
  <div class="btn-ghost" style="left:490px;top:243px;width:191px;height:49px">Read More</div>
  <h2 class="form-title">SELL YOUR HOUSE ▾</h2>
  <div class="form-rule"></div>
  <div class="field" style="left:162px;top:479px;width:272px">First Name</div>
  <div class="field" style="left:459px;top:479px;width:280px">Last Name</div>
  <div class="field" style="left:766px;top:479px;width:271px">Phone</div>
  <div class="field" style="left:162px;top:547px;width:314px">Email</div>
  <div class="field" style="left:503px;top:547px;width:403px">Property Address</div>
  <div class="btn-submit">Submit</div>
</section>

<section class="process">
  <svg class="abs" style="left:0;top:0" width="1200" height="489" viewBox="0 0 1200 489">
    <defs><marker id="arrowHead" markerWidth="12" markerHeight="12" refX="8" refY="6" orient="auto"><path d="M1 1 L9 6 L1 11" fill="none" stroke="#9aa0a6" stroke-width="1.6"/></marker></defs>
    <g fill="none" stroke="#9aa0a6" stroke-width="1.6" stroke-dasharray="6 5">
      <path d="M280 160 Q360 115 438 165" marker-end="url(#arrowHead)"/>
      <path d="M520 302 Q600 345 676 300" marker-end="url(#arrowHead)"/>
      <path d="M750 160 Q830 115 906 165" marker-end="url(#arrowHead)"/>
    </g>
  </svg>
  <div class="step-label" style="left:160px;top:125px">1. Fill In the Form</div>
  <div class="step-label" style="left:621px;top:125px">3. Find a Solution</div>
  <div class="step-circle slate" style="left:180px;top:179px">
    <svg width="56" height="56" viewBox="0 0 56 56" fill="none" stroke="#fff" stroke-width="4" stroke-linejoin="round"><rect x="10" y="10" width="32" height="40" rx="3"/><rect x="19" y="5" width="14" height="9" rx="2" fill="#3f4e5a"/><path d="M22 40 L24 33 L42 15 L47 20 L29 38 Z"/></svg>
  </div>
  <div class="step-circle red" style="left:416px;top:179px">
    <svg width="56" height="56" viewBox="0 0 24 24" fill="none" stroke="#fff" stroke-width="1.8" stroke-linejoin="round"><path d="M6.6 10.8a15 15 0 0 0 6.6 6.6l2.2-2.2a1 1 0 0 1 1-.25 11.4 11.4 0 0 0 3.6.57 1 1 0 0 1 1 1V20a1 1 0 0 1-1 1A17 17 0 0 1 3 4a1 1 0 0 1 1-1h3.5a1 1 0 0 1 1 1c0 1.25.2 2.45.57 3.57a1 1 0 0 1-.25 1z"/><path d="M20 4 L14 10 M14 5 V10 H19" stroke-linecap="round"/></svg>
  </div>
  <div class="step-circle slate" style="left:649px;top:179px">
    <svg width="56" height="56" viewBox="0 0 56 56" fill="none" stroke="#fff" stroke-width="4" stroke-linejoin="round"><path d="M12 20 H22 a5 5 0 1 1 10 0 H40 V30 a5 5 0 1 1 0 10 V46 H12 V38 a5 5 0 1 0 0-10 Z" transform="rotate(-35 28 32)"/></svg>
  </div>
  <div class="step-circle red" style="left:883px;top:179px">
    <svg width="56" height="56" viewBox="0 0 56 56" fill="none" stroke="#fff" stroke-width="4" stroke-linejoin="round"><path d="M21 8 H35 L31 16 H25 Z"/><path d="M25 16 C12 24 10 48 28 48 C46 48 44 24 31 16"/><text x="28" y="41" text-anchor="middle" font-size="18" font-weight="700" fill="#fff" stroke="none" font-family="Source Sans 3, sans-serif">$</text></svg>
  </div>
  <div class="step-label red" style="left:379px;top:339px;width:200px">2. Get a Call within<br>24 hours</div>
  <div class="step-label red" style="left:846px;top:339px;width:200px">4. Go on with<br>Your Life</div>
</section>

<section class="we-buy" role="img" aria-label="Photo of a single-storey house with a front lawn under a red overlay">
  <h2 class="section-title" style="left:467px;top:100px">WE BUY HOUSES</h2>
  <p class="we-buy-sub">I need to sell my House, and Fast!</p>
  <p class="we-buy-text">This is Photoshop's version &nbsp;of Lorem Ipsum. Proin gravida nibh vel velit auctor aliquet. Aenean sollicitudin, lorem quis bibendum auctor, nisi elit consequat ipsum, nec sagittis sem nibh id elit. Duis sed odio sit amet ni h vulputate cursus a sit amet mauris. Morbi.</p>
  <div class="btn-ghost" style="left:877px;top:428px;width:160px;height:42px">Read More</div>
</section>

<section class="features">
  <h2>Lorem Ipsum Proin gravida nibh</h2>
  <p class="features-lead">This is Photoshop's version &nbsp;of Lorem Ipsum. Proin gravida nibh vel velit auctor aliquet. Aenean sollicitudin, lorem quis bibendum auctor, nisi elit consequat ipsum, nec</p>
  <ul class="bullet-list">
    <li>We pay cash</li>
    <li>We pay regular closing costs</li>
    <li>We buy houses as is</li>
    <li>No unreasonable home buyer demands</li>
    <li>Fast closings so you can move out and move on</li>
  </ul>
  <svg class="features-mark" viewBox="0 0 470 380" aria-label="Lurt Takes Homes">
    <rect x="40" y="130" width="120" height="120" fill="#e8302f"/>
    <text x="190" y="178" font-family="Source Sans 3, sans-serif" font-size="44" font-weight="700" fill="#3f4e5a">Lurt Takes</text>
    <text x="190" y="232" font-family="Source Sans 3, sans-serif" font-size="44" font-weight="700" fill="#3f4e5a">Homes</text>
  </svg>
</section>

<section class="clients" role="img" aria-label="Photo of two people shaking hands in front of a house, darkened">
  <h2 class="section-title" style="left:0;width:1200px;text-align:center;top:96px">OUR CLIENTS</h2>
  <div class="quote-mark" style="left:166px;top:165px">&ldquo;</div>
  <p class="clients-text">Lorem Ipsum is simply dummy text of the printing and typesetting industry. Lorem Ipsum has been the industry's standard dummy text ever since the 1500s Lorem Ipsum is simply dummy text of the printing and typesetting industry.</p>
  <div class="quote-mark" style="left:962px;top:282px">&rdquo;</div>
  <svg class="abs" style="left:322px;top:380px" width="24" height="36" viewBox="0 0 24 36"><path d="M20 3 L5 18 L20 33" fill="none" stroke="#fff" stroke-width="5"/></svg>
  <svg class="abs" style="left:866px;top:380px" width="24" height="36" viewBox="0 0 24 36"><path d="M4 3 L19 18 L4 33" fill="none" stroke="#fff" stroke-width="5"/></svg>
  <div class="client-avatar" role="img" aria-label="Portrait of the client"></div>
  <p class="client-name">Daniel R. Hale</p>
</section>

<footer class="site-footer">
  <div class="footer-skyline" role="img" aria-label="City skyline silhouette"></div>
  <h3 class="footer-head" style="left:162px">About Us</h3>
  <h3 class="footer-head" style="left:563px">Navigations</h3>
  <h3 class="footer-head" style="left:888px">Join Us</h3>
  <div class="footer-rule"></div>
  <p class="footer-about">We help owners sell houses in any condition. We pay cash, cover closing costs and buy as is. Tell us about your property and we will call you within one day with a fair offer and clear options, so you can move on quickly.</p>
  <ul class="footer-nav">
    <li>Home</li><li>Sell My House</li><li>Recent Projects</li><li>How it Works</li><li>About</li>
  </ul>
  <div class="footer-social" aria-label="Social links"><span></span><span></span><span></span><span></span><span></span></div>
  <div class="footer-brand"><i></i><span>Lurt Takes Homes</span></div>
  <p class="footer-copy">© 2014 Lurt Takes Homes<br>All Rights Reserved</p>
</footer>

</body>
</html>
```